qoVantix Employee-Centric Engagement brochure

Design a 2-page 81/2" x 11'' brochure (front and back) that includes our logo and some pictures. We need it in a format that we can print from and edit. Word or PDF would be good. We need to be able to give the file to a printing company or ShipLark office for them to print for us. We conduct frequent employee surveys as well as providing coaching to employees and managers around the data. Our goal is to get employees engaged in continuous improvement and in making their teams and workplace the best it can be. We have been in business for 20 years and this is an extension of what we have been doing in the past. Bringing the ownership of engagement and improvement to the employees rather than having managers responsible for employee engagement and process improvement. Our Energy metric is research based and predicts performance. Our web site is www.qovantix.example. I've attached a Word document with our first pass at content. Please improve greatly on this.

Target Market(s)

Company managers and senior HR personnel

Industry/Entity Type

Employee

Font styles to use
Sans Serif

Colors

Designer to choose colors to be used in the design.

Requirements
Must have
• All of the information in the documents sent and some appropriate pictures/background

```html
<!DOCTYPE html>
<html lang="en">
<head>
<meta charset="utf-8">
<title>qoVantix brochure</title>
<link rel="stylesheet" href="https://fonts.googleapis.com/css2?family=Roboto+Condensed:wght@400;700&family=Source+Sans+3:wght@400;600;700&display=swap">
<style>
:root{
  --bg:#e9e7e3;
  --paper:#ffffff;
  --panel:#e6e7e9;
  --blue:#1e9ad9;
  --blue-deep:#1a74b8;
  --orange:#f27a21;
  --orange-light:#f7a03a;
  --ink:#3d3d3f;
  --ink-soft:#555658;
  --teal:#19a9b8;
  --navy:#143a5a;
  --sans:"Source Sans 3",Arial,sans-serif;
  --cond:"Roboto Condensed","Arial Narrow",sans-serif;
}
*{box-sizing:border-box;margin:0;padding:0}
html,body{width:1200px;height:923px;overflow:hidden;background:var(--bg)}
body{position:relative;font-family:var(--sans);color:var(--ink)}
.page{position:absolute;width:496px;height:641px;background:var(--paper);overflow:hidden;box-shadow:0 3px 10px rgba(0,0,0,.25)}
.page--front{left:63px;top:82px}
.page--back{left:631px;top:192px}
.page__art{position:absolute;inset:0}
.abs{position:absolute}
.brand{left:22px;top:296px}
.brand__name{font-family:var(--sans);font-weight:600;font-size:38px;line-height:44px;color:var(--ink);letter-spacing:.5px}
.headline{font-family:var(--cond);font-weight:400;font-size:20px;line-height:28px;color:var(--ink);text-transform:uppercase}
.headline b{font-weight:700}
.front-headline{left:17px;top:384px}
.front-lead{left:17px;top:458px;width:250px;font-size:11.8px;line-height:18px;color:var(--ink)}
.tag{height:32px;background:var(--blue);color:#fff;font-size:17px;line-height:32px;padding-left:12px;clip-path:polygon(0 0,100% 0,94% 100%,0 100%);box-shadow:0 3px 4px rgba(0,0,0,.15)}
.tag--moving{left:277px;top:209px;width:194px}
.tag--proven{left:277px;top:403px;width:194px}
.ticks{list-style:none;font-size:9.8px;line-height:12px;color:var(--ink-soft);width:200px}
.ticks li{position:relative;padding-left:14px;margin-bottom:4.5px}
.ticks li::before{content:"";position:absolute;left:0;top:2px;width:6px;height:6px;border:1px solid var(--blue);border-radius:50%}
.ticks li::after{content:"";position:absolute;left:2.5px;top:3.5px;width:2px;height:3px;border:solid var(--blue);border-width:0 1px 1px 0;transform:rotate(40deg)}
.ticks--moving{left:288px;top:257px}
.ticks--proven{left:288px;top:450px}
.contact{left:19px;top:586px;color:#fff;font-size:12.5px;line-height:17px}
.contact b{font-weight:700}
.back-title{left:17px;top:283px}
.back-body{left:17px;top:372px;width:210px;font-size:10.3px;line-height:13.8px;text-align:justify;color:var(--ink)}
.process-title{left:257px;top:210px;font-size:13px;color:#222}
.step-label{left:396px;width:100px;font-size:8.4px;line-height:10.4px;color:var(--ink-soft)}
.process-close{left:257px;top:517px;width:220px;font-size:11px;line-height:13.5px;color:#222}
.num{font-family:var(--cond);font-size:24px;fill:#fff}
</style>
</head>
<body>

<section class="page page--front" aria-label="Front page">
  <svg class="page__art" viewBox="0 0 496 641">
    <defs>
      <linearGradient id="photoFront" x1="0" y1="0" x2="1" y2="1">
        <stop offset="0" stop-color="#c9d6e3"/><stop offset=".5" stop-color="#e8eef3"/><stop offset="1" stop-color="#b7c8d8"/>
      </linearGradient>
      <linearGradient id="bandBlue" x1="0" y1="0" x2="1" y2="0">
        <stop offset="0" stop-color="#1e9ad9"/><stop offset="1" stop-color="#2aa6e2"/>
      </linearGradient>
      <linearGradient id="bandOrange" x1="0" y1="0" x2="1" y2="0">
        <stop offset="0" stop-color="#f7a03a"/><stop offset="1" stop-color="#f26a21"/>
      </linearGradient>
    </defs>
    <rect x="281" y="200" width="215" height="400" fill="var(--panel)"/>
    <path d="M0 0H496V196Q260 185 0 252Z" fill="url(#photoFront)" role="img" aria-label="Photo of a cheerful business team applauding around a laptop"/>
    <path d="M0 258Q250 190 496 198V206Q250 205 0 282Z" fill="url(#bandOrange)"/>
    <path d="M0 534Q210 585 440 641H0Z" fill="url(#bandBlue)"/>
    <path d="M360 641Q450 600 496 540V552Q455 610 380 641Z" fill="var(--blue-deep)"/>
    <path d="M380 641Q460 612 496 560V641Z" fill="url(#bandOrange)"/>
  </svg>

  <div class="abs brand"><span class="brand__name">qoVantix</span></div>

  <h1 class="abs headline front-headline"><b>Focus employee energy</b><br>on what really matters</h1>
  <p class="abs front-lead">Managers delegate, coach and teach. Ambassadors are facilitators and co-creators. Employees are agents of change and improvement.</p>

  <div class="abs tag tag--moving">by moving up to</div>
  <ul class="abs ticks ticks--moving">
    <li>Empowering employees to own their own engagement and energy</li>
    <li>Managers are teachers and advisors vs. survey interpreters</li>
    <li>On-going and frequent process built the way you do business</li>
    <li>Backed by the science of human energy at work</li>
    <li>Documented return on investment (ROI)</li>
  </ul>

  <div class="abs tag tag--proven">simple » fast » proven</div>
  <ul class="abs ticks ticks--proven">
    <li>Transforming employee engagement with a proven model</li>
    <li>Simple and fast implementation</li>
    <li>Quick and easy process for users</li>
    <li>Celebrations focused on documented results</li>
  </ul>

  <p class="abs contact">Call today: <b>+1 555-014-2270,</b><br>or right to <b>info@qovantix.example</b><br><b>www.qovantix.example</b></p>
</section>

<section class="page page--back" aria-label="Back page">
  <svg class="page__art" viewBox="0 0 496 641">
    <defs>
      <linearGradient id="photoBack" x1="0" y1="0" x2="1" y2="1">
        <stop offset="0" stop-color="#d9d3cc"/><stop offset=".5" stop-color="#eef0f2"/><stop offset="1" stop-color="#c46a55"/>
      </linearGradient>
      <linearGradient id="bandBlue2" x1="0" y1="0" x2="1" y2="0">
        <stop offset="0" stop-color="#1e9ad9"/><stop offset="1" stop-color="#2aa6e2"/>
      </linearGradient>
      <linearGradient id="bandOrange2" x1="0" y1="0" x2="1" y2="0">
        <stop offset="0" stop-color="#f7a03a"/><stop offset="1" stop-color="#f26a21"/>
      </linearGradient>
      <linearGradient id="panelBack" x1="0" y1="0" x2="0" y2="1">
        <stop offset="0" stop-color="#e4e5e7"/><stop offset="1" stop-color="#ffffff"/>
      </linearGradient>
      <linearGradient id="shade" x1="0" y1="0" x2="1" y2="1">
        <stop offset="0" stop-color="#000" stop-opacity=".18"/><stop offset="1" stop-color="#000" stop-opacity="0"/>
      </linearGradient>
    </defs>
    <rect x="0" y="170" width="496" height="400" fill="url(#panelBack)"/>
    <path d="M0 0H496V180Q250 175 0 245Z" fill="url(#photoBack)" role="img" aria-label="Photo of colleagues in a lounge reviewing documents together"/>
    <path d="M0 252Q250 178 496 182V190Q250 195 0 275Z" fill="url(#bandOrange2)"/>

    <g stroke="#b9bcc0" stroke-width="1.2">
      <line x1="300" y1="277" x2="381" y2="277"/>
      <line x1="345" y1="322" x2="381" y2="322"/>
      <line x1="300" y1="371" x2="381" y2="371"/>
      <line x1="345" y1="418" x2="381" y2="418"/>
      <line x1="300" y1="465" x2="381" y2="465"/>
    </g>
    <g fill="#b9bcc0">
      <circle cx="382" cy="277" r="5"/><circle cx="382" cy="322" r="5"/><circle cx="382" cy="371" r="5"/><circle cx="382" cy="418" r="5"/><circle cx="382" cy="465" r="5"/>
    </g>
    <g stroke-width="8">
      <line x1="300" y1="290" x2="320" y2="309" stroke="var(--teal)"/>
      <line x1="320" y1="336" x2="300" y2="356" stroke="#1b5d95"/>
      <line x1="300" y1="384" x2="320" y2="404" stroke="var(--navy)"/>
      <line x1="320" y1="431" x2="300" y2="451" stroke="#232325"/>
    </g>

    <g>
      <path d="M288 277l40 40l-20 20l-40-40z" fill="url(#shade)"/>
      <path d="M333 322l40 40l-20 20l-40-40z" fill="url(#shade)"/>
      <path d="M288 371l40 40l-20 20l-40-40z" fill="url(#shade)"/>
      <path d="M333 418l40 40l-20 20l-40-40z" fill="url(#shade)"/>
      <path d="M289 465l40 40l-20 20l-40-40z" fill="url(#shade)"/>
    </g>
    <g stroke="#fff" stroke-width="3">
      <path d="M288 246l31 31l-31 31l-31-31z" fill="#1c7bb0"/>
      <path d="M333 291l31 31l-31 31l-31-31z" fill="var(--teal)"/>
      <path d="M288 340l31 31l-31 31l-31-31z" fill="#1b5d95"/>
      <path d="M333 387l31 31l-31 31l-31-31z" fill="var(--navy)"/>
      <path d="M289 434l31 31l-31 31l-31-31z" fill="#232325"/>
    </g>
    <g class="num" text-anchor="middle">
      <text x="288" y="286">01</text><text x="333" y="331">02</text><text x="288" y="380">03</text><text x="333" y="427">04</text><text x="289" y="474">05</text>
    </g>

    <path d="M0 534Q210 585 440 641H0Z" fill="url(#bandBlue2)"/>
    <path d="M360 641Q450 600 496 540V552Q455 610 380 641Z" fill="var(--blue-deep)"/>
    <path d="M380 641Q460 612 496 560V641Z" fill="url(#bandOrange2)"/>
  </svg>

  <p class="abs process-title">Employee-centric engagement process</p>
  <p class="abs step-label" style="top:260px">Frequent pulsing<br>(3 to 5 questions to<br>spark learning)</p>
  <p class="abs step-label" style="top:311px">Employees review<br>trend data and journal</p>
  <p class="abs step-label" style="top:361px">Ambassadors guide<br>improvement dialogue</p>
  <p class="abs step-label" style="top:408px">3 ideas presented<br>to manager</p>
  <p class="abs step-label" style="top:455px">Manager helps facili-<br>tate implementation</p>

  <h2 class="abs headline back-title"><b>It works<br>not a survey</b><br>learning for all</h2>
  <p class="abs back-body">Employee-centric engagement uses a new lens to bring people together to drive positive change. Through a data-driven process, frequent pulsing is focused on the employee learning from their own data. Employees learn and reflect and then engage with peer ambassadors who use root-cause analysis, ideation and other tools to focus learning and present 3 improvement ideas to managers. Return on investment projections are done for each idea.</p>
  <p class="abs process-close">Enhance firm performance by changing how your business listens and learns.</p>

  <p class="abs contact">Call today: <b>+1 555-014-2270,</b><br>or right to <b>info@qovantix.example</b><br><b>www.qovantix.example</b></p>
</section>

</body>
</html>
```